Non-profit for Addiction Counselors Needs Flyer & PowerPoint Slide Template for Learning Collab

We need a flyer and PowerPoint Slide template design for a non-profit organization based in Washington, DC called "KORVELT, The Guild for Recovery Practitioners". We are partnering with an organization called Sol Marena to provide "The Clinic Growth Practice Exchange Program" that helps organizations maximize current funding and service opportunities inherent in healthcare reform and identify and address barriers to growth. The designs should be co-branded for both KORVELT and Sol Marena, with KORVELT represented first.

KORVELT, the Guild for Recovery Practitioners, represents the professional interests of more than 75,000 addiction counselors, educators and other addiction-focused health care professionals in the United States, Canada and abroad. KORVELT’s members are addiction counselors, educators and other addiction-focused health care professionals, who specialize in addiction prevention, treatment, recovery support and education. An important part of the healthcare continuum, KORVELT members and its 44 state affiliates work to create healthier individuals, families and communities through prevention, intervention, quality treatment and recovery support.

The purpose of the flyer is to promote and recruit customers to join the Learning Collaborative.

We would like to see designs that use blue, the main color of our website (www.korvelt-guild.example) and fit nicely with the colors of the Sol Marena logo (gray and blue).

The final design should communicate professionalism and there is a great benefit to the organization for buying this product/joining this Collaborative.

Target Market(s)

Our membership potentials are addiction counselors or administrators of addiction treatment centers, women and men, aged 30 to 65 who are all trained as therapists and care about people.

Industry/Entity Type

Non-Profit

Font styles to use
Sans Serif

Colors
3377b5
cedeec
eaf1f7
5c5c5c

Requirements
Must have
• Package must include two pieces: promotional flyer and PowerPoint slide deck template.

Flyer: The flyer must be one page, be easy to read and clear, yet bright and colorful, and must appear best on the computer screen or opened on a tablet - most views will be online, with a small portion printed for handing out at conferences. Must have graphics - if a group of people, must be culturally diverse.

PowerPoint: Need main title slide, transition slide and main content slide templates that are coordinated with the flyer design elements or vice versa

Everything must contain our two logos - three are attached to choose from.
Everything must be clean and modern/contemporary in tone.

I included a sample application that I created for this project that shows what we have done so far, and how we wish to use the "combo logo" on other pieces created for this project.

```html
<!DOCTYPE html>
<html lang="en">
<head>
<meta charset="utf-8">
<title>The Clinic Growth Practice Exchange Program</title>
<link href="https://fonts.googleapis.com/css2?family=Ubuntu:ital,wght@0,300;0,400;0,500;0,700;1,400;1,500&display=swap" rel="stylesheet">
<style>
  :root {
    --brand-blue: #2f7bbf;
    --deep-blue: #1f6aae;
    --pale-blue: #cedeec;
    --mist: #eaf1f7;
    --ink: #5c5c5c;
    --soft-gray: #e9e9e9;
    --logo-gray: #4a4a4a;
    --white: #ffffff;
  }
  * { box-sizing: border-box; margin: 0; padding: 0; }
  html, body { width: 848px; height: 1200px; overflow: hidden; background: var(--white); }
  body { font-family: "Ubuntu", Arial, sans-serif; color: var(--ink); }
  .flyer { position: relative; width: 848px; height: 1200px; background: var(--white); overflow: hidden; }

  .hero { position: absolute; left: 0; top: 0; width: 848px; height: 384px; box-shadow: 0 6px 8px rgba(0,0,0,0.18); }
  .hero-panel { position: absolute; left: 0; top: 0; width: 322px; height: 384px; background: var(--brand-blue); padding: 44px 18px 0 22px; }
  .hero-title { color: var(--white); font-weight: 700; font-size: 42px; line-height: 38px; letter-spacing: -0.5px; }
  .hero-tagline { margin-top: 30px; color: var(--white); font-style: italic; font-weight: 500; font-size: 15px; line-height: 18px; }
  .hero-photo { position: absolute; left: 322px; top: 0; width: 526px; height: 384px;
    background: linear-gradient(180deg, #f3f5f6 0%, #e6eaed 45%, #d4d9dc 100%); }

  .intro { position: absolute; left: 36px; top: 424px; width: 566px; font-size: 15.6px; line-height: 19.2px; text-align: justify; font-weight: 400; }
  .intro-photo { position: absolute; left: 624px; top: 424px; width: 196px; height: 250px; border-radius: 12px;
    background: linear-gradient(180deg, #f4f6f8 0%, #e3e8ec 55%, #c9cfd5 100%); box-shadow: 0 3px 6px rgba(0,0,0,0.2); }

  .focus-tab { position: absolute; left: 0; top: 718px; width: 510px; height: 48px; background: var(--deep-blue);
    color: var(--white); font-weight: 500; font-size: 23.5px; line-height: 48px; padding-left: 34px; }
  .focus-list { position: absolute; left: 34px; top: 780px; width: 770px; list-style: none; font-size: 15.6px; line-height: 19px; }
  .focus-list li { position: relative; padding-left: 20px; margin-bottom: 9px; }
  .focus-list svg { position: absolute; left: 0; top: 2px; width: 15px; height: 15px; }

  .promise { position: absolute; left: 17px; top: 982px; width: 816px; height: 58px; background: var(--soft-gray);
    color: var(--deep-blue); font-weight: 700; font-size: 16.4px; line-height: 21px; text-align: center; padding-top: 8px; }

  .footer-band { position: absolute; left: 0; top: 1182px; width: 848px; height: 18px; background: var(--brand-blue); }
  .register-card { position: absolute; left: 40px; top: 1062px; width: 768px; height: 120px; background: var(--white);
    border-radius: 34px 34px 0 0; box-shadow: 0 -3px 8px rgba(0,0,0,0.18); }
  .register-title { position: absolute; left: 24px; top: 20px; color: var(--deep-blue); font-weight: 500; font-size: 34px; }
  .register-note { position: absolute; left: 24px; top: 64px; font-size: 14px; line-height: 17px; }
  .partner-korvelt { position: absolute; left: 308px; top: 20px; width: 168px; height: 82px; background: var(--deep-blue);
    color: var(--white); font-weight: 700; font-size: 24px; display: flex; align-items: center; justify-content: center; gap: 8px; }
  .partner-korvelt .mark { width: 12px; height: 12px; background: var(--white); }
  .partner-sol { position: absolute; left: 480px; top: 20px; width: 254px; height: 82px; background: var(--logo-gray);
    color: var(--white); font-weight: 400; font-size: 20px; letter-spacing: 2px; display: flex; align-items: center; justify-content: center; }
</style>
</head>
<body>
<main class="flyer">
  <header class="hero">
    <div class="hero-panel">
      <h1 class="hero-title">The Clinic Growth Practice Exchange Program</h1>
      <p class="hero-tagline">Elevating and Focusing Addiction, Co-Occurring and Recovery Business Practices for Sustainability, Fiscal Strength, Clinical Excellence, Recovery Orientation and Industry Leadership</p>
    </div>
    <div class="hero-photo" role="img" aria-label="Photo of a diverse group of professionals seated in a circle in discussion"></div>
  </header>

  <section class="intro">
    <p>Most addiction and co-occurring treatment agencies are evaluating how to help ensure their agency's viability, sustainability, funding, and seeking growth opportunities within this evolving landscape. Get the education, guidance, and consultation your organization needs from those who know it best!</p>
    <p>The Clinic Growth Practice Exchange Program is an intensive, interactive program that is designed to help your organization maximize current funding and service opportunities inherent in healthcare reform and identify and address barriers to growth. Over six months, participants will receive training and consulting directly from industry leaders, highly successful provider CEOs, and national subject matter experts through live webinars, fireside chats, and private consultation. With hands-on guidance, participants will develop a concise, easy to follow, and comprehensive sustainability and growth plan for their organization using a proven and effective sustainability and growth template.</p>
  </section>
  <div class="intro-photo" role="img" aria-label="Photo of a smiling professional in a suit with arms crossed, colleagues behind"></div>

  <h2 class="focus-tab">This Learning Collaborative will focus on:</h2>
  <ul class="focus-list">
    <li><svg viewBox="0 0 15 15"><rect x="1" y="3" width="11" height="11" fill="none" stroke="#2f7bbf" stroke-width="1.5"/><path d="M3.5 8 L6.5 11 L13.5 2" fill="none" stroke="#2f7bbf" stroke-width="2"/></svg>Increasing funding and sustainability</li>
    <li><svg viewBox="0 0 15 15"><rect x="1" y="3" width="11" height="11" fill="none" stroke="#2f7bbf" stroke-width="1.5"/><path d="M3.5 8 L6.5 11 L13.5 2" fill="none" stroke="#2f7bbf" stroke-width="2"/></svg>Understanding and effectively working with third party payers (federal, state, managed care and insurance companies)</li>
    <li><svg viewBox="0 0 15 15"><rect x="1" y="3" width="11" height="11" fill="none" stroke="#2f7bbf" stroke-width="1.5"/><path d="M3.5 8 L6.5 11 L13.5 2" fill="none" stroke="#2f7bbf" stroke-width="2"/></svg>Developing strategic partnerships (such as with ACO’s, Health Homes, Group Practices, FQHC, Recovery Organizations, and hospital systems)</li>
    <li><svg viewBox="0 0 15 15"><rect x="1" y="3" width="11" height="11" fill="none" stroke="#2f7bbf" stroke-width="1.5"/><path d="M3.5 8 L6.5 11 L13.5 2" fill="none" stroke="#2f7bbf" stroke-width="2"/></svg>Learning how to access grants and manage contracts while insuring back-office business practices are in place to meet current demands</li>
    <li><svg viewBox="0 0 15 15"><rect x="1" y="3" width="11" height="11" fill="none" stroke="#2f7bbf" stroke-width="1.5"/><path d="M3.5 8 L6.5 11 L13.5 2" fill="none" stroke="#2f7bbf" stroke-width="2"/></svg>Executive leadership development and so much more!</li>
  </ul>

  <p class="promise">KORVELT and Sol Marena know where the opportunities are and how to help you get to them. We will be holding nothing back to help insure your success -- for you as an executive leader and for your agency.</p>

  <section class="register-card">
    <h2 class="register-title">Register today!</h2>
    <p class="register-note">Space is limited. Registration closes<br>Wednesday, April 17, 2014!</p>
    <div class="partner-korvelt"><span class="mark"></span>KORVELT</div>
    <div class="partner-sol">SOL MARENA, LLC</div>
  </section>
  <div class="footer-band"></div>
</main>
</body>
</html>
```